Atelier Marrow Architecture business card

We need to update our business card. We do high end custom residential, hospitality, and wellness architecture. We focus on creating unique spaces and design around the five senses, believing that architecture's true impact is not on our surroundings, but within us. We would like to see designs are instill a sense of calm awe. They should be crisp, fresh, clean, authentic, & contemporary without being sterile, overworked, or harsh. White space is important. Alternative materials are an option if natural. We have created our own logo and would like designs to incorporate it. However, we are willing to see alternatives if the logo becomes a stumbling block and you have an alternate you suggest. Card must have the following information:
Atelier Marrow Architecture, Inc.
728 Holloway Ct. NE Atlanta, GA 30318
Marcus T. Whitcombe, AIA, NCARB, LEED AP BD+C
ateliermarrow.example

Target Market(s)

Higher net worth individuals with an appreciation for design, nature, sustainability,

Industry/Entity Type

Architect

Contact Information for Business Card

See above. The title of Owner or Architect is helpful but not necessary. Minimalism should trump additional information.

Font styles to use
Serif
Sans Serif

Requirements
Must have
• It should look professional. It must use logo
Should not have
• caligraphy, animals, anything that is cute,

```html
<!DOCTYPE html>
<html lang="en">
<head>
<meta charset="utf-8">
<title>Atelier Marrow Architecture — Business Card</title>
<link href="https://fonts.googleapis.com/css2?family=PT+Serif:wght@400;700&display=swap" rel="stylesheet">
<style>
  :root {
    --backdrop: #e4e4e2;
    --card: #ffffff;
    --green: #137a1f;
    --green-deep: #0e6a18;
    --ink: #3a3a3a;
    --muted: #6b6b6b;
    --rule: #dcdcdc;
    --charcoal: #333333;
  }
  * { box-sizing: border-box; margin: 0; padding: 0; }
  html, body {
    width: 1200px; height: 1000px; overflow: hidden;
    background: var(--backdrop);
    font-family: "PT Serif", Georgia, serif;
  }
  .card {
    position: absolute; left: 220px; width: 760px;
    background: var(--card); border-radius: 28px; overflow: hidden;
    box-shadow: 0 6px 18px rgba(0,0,0,0.18);
  }
  .card--front { top: 50px; height: 433px; }
  .card--back { top: 523px; height: 437px; }

  .wordmark {
    position: absolute; color: var(--ink); font-weight: 400;
    text-transform: uppercase; white-space: nowrap;
    display: flex; align-items: center;
  }
  .wordmark__square {
    display: inline-block; background: var(--green);
  }
  .card--front .wordmark {
    left: 0; right: 0; top: 212px; justify-content: center;
    font-size: 30px; letter-spacing: 5px;
  }
  .card--front .wordmark__square { width: 22px; height: 22px; margin-right: 18px; }

  .card--back .wordmark {
    right: 44px; top: 55px; font-size: 19px; letter-spacing: 3.5px;
  }
  .card--back .wordmark__square { width: 14px; height: 14px; margin-right: 12px; }

  .front-url {
    position: absolute; left: 0; right: 0; top: 366px;
    text-align: center; font-size: 16px; color: var(--muted); letter-spacing: 0.3px;
  }

  .name-tab {
    position: absolute; left: 0; top: 213px; width: 12px; height: 40px;
    background: var(--green); border-radius: 0 5px 5px 0;
  }
  .person { position: absolute; left: 44px; top: 207px; }
  .person__name { font-size: 22px; font-weight: 700; color: var(--green); line-height: 1.2; }
  .person__credentials { font-size: 16px; color: var(--muted); margin-top: 4px; }

  .divider {
    position: absolute; left: 44px; right: 43px; top: 272px;
    border-top: 1.5px solid var(--rule);
  }

  .contact-list {
    position: absolute; left: 44px; top: 287px; list-style: none;
    font-size: 16px; color: var(--muted); line-height: 22px;
  }
  .contact-list li { display: flex; align-items: center; }
  .contact-list svg { width: 14px; height: 14px; margin-right: 8px; fill: var(--green); }

  .office {
    position: absolute; right: 42px; top: 306px; text-align: right;
    font-size: 16px; color: var(--muted); line-height: 22px;
  }
  .office__company { font-weight: 700; color: var(--green); }

  .footer-rule {
    position: absolute; left: 0; right: 0; top: 402px; height: 3px; background: var(--charcoal);
  }
  .footer-band {
    position: absolute; left: 0; right: 0; top: 410px; bottom: 0;
    background: linear-gradient(90deg, var(--green-deep), var(--green) 60%, #1d8a2a);
  }
</style>
</head>
<body>

<section class="card card--front" aria-label="Card front">
  <div class="wordmark"><span class="wordmark__square"></span>Atelier Marrow Architecture</div>
  <p class="front-url">www.ateliermarrow.example</p>
</section>

<section class="card card--back" aria-label="Card back">
  <div class="wordmark"><span class="wordmark__square"></span>Atelier Marrow Architecture</div>

  <span class="name-tab"></span>
  <div class="person">
    <p class="person__name">Marcus T. Whitcombe</p>
    <p class="person__credentials">AIA, NCARB, LEED AP BD+C</p>
  </div>

  <div class="divider"></div>

  <ul class="contact-list">
    <li>
      <svg viewBox="0 0 16 16" aria-hidden="true"><path d="M3.5 1.5l2.5 0 1 3.5-1.6 1.2a9 9 0 0 0 4.4 4.4l1.2-1.6 3.5 1v2.5c0 .8-.7 1.5-1.5 1.5C7 14 2 9 2 3c0-.8.7-1.5 1.5-1.5z"/></svg>
      404.555.0142
    </li>
    <li>
      <svg viewBox="0 0 16 16" aria-hidden="true"><path d="M4 1h8v4H4z"/><path d="M1 6h14v6h-3v-2H4v2H1z"/><path d="M5 11h6v4H5z"/></svg>
      404.555.0187
    </li>
    <li>
      <svg viewBox="0 0 16 16" aria-hidden="true"><path d="M1 3h14v1.2L8 9 1 4.2z"/><path d="M1 5.8l7 4.8 7-4.8V13H1z"/></svg>
      info@ateliermarrow.example
    </li>
    <li>
      <svg viewBox="0 0 16 16" aria-hidden="true"><path d="M8 1a7 7 0 1 0 0 14A7 7 0 0 0 8 1zm0 1.4c.8.8 1.5 2.2 1.8 3.8H6.2C6.5 4.6 7.2 3.2 8 2.4zM2.6 7.4h2.5v1.2H2.6zm3.6 0h3.6v1.2H6.2zm4.7 0h2.5v1.2h-2.5zM6.2 9.8h3.6c-.3 1.6-1 3-1.8 3.8-.8-.8-1.5-2.2-1.8-3.8z"/></svg>
      www.ateliermarrow.example
    </li>
  </ul>

  <address class="office" style="font-style: normal;">
    <p class="office__company">Atelier Marrow Architecture, Inc.</p>
    <p>728 Holloway Ct. NE</p>
    <p>Atlanta, GA 30318</p>
  </address>

  <div class="footer-rule"></div>
  <div class="footer-band"></div>
</section>

</body>
</html>
```